need 4 creative A frame (SANDWICH BOARD) designs concepts for dental office

need 4 creative A frame (SANDWICH BOARD) designs concepts
1 - targeting kids
2. targeting old age
3. targeting teens
4 targeting general public

website - www.brenvaxdental.ca

LINK for Measurements for sandwich board https://www.korvepa.ca/BL_1921/Aluminum-Snap-Edge-A-Frame-Sign

i am attaching certain key ingredients ( rough sketch in uploaded files ) to be added on each design though not mandatory if the design is very creative

```html
<!DOCTYPE html>
<html lang="en">
<head>
<meta charset="utf-8">
<title>Brenvax Dental – A-Frame Sign Concepts</title>
<link href="https://fonts.googleapis.com/css2?family=Oswald:wght@300;400;600;700&family=Roboto:wght@400;500;700&family=Roboto+Slab:wght@700&family=Noto+Serif:wght@400&display=swap" rel="stylesheet">
<style>
  :root {
    --teal: #1a9a9a;
    --teal-deep: #13807f;
    --teal-dark: #14666c;
    --teal-light: #5fc6c4;
    --aqua: #27d3cf;
    --page: #eeeeee;
    --white: #ffffff;
    --red: #e0202a;
    --grey: #9aa3a6;
  }
  * { box-sizing: border-box; margin: 0; padding: 0; }
  html, body { width: 1200px; height: 656px; overflow: hidden; background: var(--page); }
  .canvas { position: relative; width: 1200px; height: 656px; }

  .board { position: absolute; top: 123px; height: 409px; overflow: hidden; }
  .board--kids    { left: 22px;  width: 290px; background: linear-gradient(180deg, var(--teal) 0%, #7fd2cf 45%, #f4fbfa 72%, var(--white) 100%); }
  .board--teens   { left: 312px; width: 287px; background: var(--teal); }
  .board--seniors { left: 599px; width: 288px; background: var(--white); }
  .board--general { left: 888px; width: 289px; background: #f3f4f4; }

  .abs { position: absolute; }

  .headline { font-family: "Oswald", sans-serif; line-height: 1; text-transform: uppercase; white-space: nowrap; }
  .headline__main { display: block; font-weight: 700; font-size: 20px; }
  .headline__sub  { display: block; font-weight: 300; font-size: 16.5px; margin-top: 3px; }

  .brand { font-family: "Oswald", sans-serif; font-weight: 400; color: var(--teal); font-size: 19px; line-height: 1; white-space: nowrap; display: flex; align-items: center; gap: 5px; }
  .brand--stacked { font-size: 14px; line-height: 1.05; }
  .brand__dot { width: 9px; height: 9px; border-radius: 50%; background: var(--teal-light); display: inline-block; flex: none; }

  .feature { display: flex; align-items: center; gap: 4px; font-family: "Oswald", sans-serif; font-weight: 600; font-size: 9.5px; line-height: 0.95; color: var(--teal-dark); text-transform: uppercase; }
  .feature svg { flex: none; }

  .were-in { font-family: "Oswald", sans-serif; font-weight: 700; text-transform: uppercase; line-height: 1; }
  .welcome-serif { font-family: "Roboto Slab", serif; font-weight: 700; line-height: 1.05; }
  .welcome-sans { font-family: "Roboto", sans-serif; font-weight: 500; }
  .phone-serif { font-family: "Noto Serif", serif; font-weight: 400; display: flex; align-items: center; gap: 3px; }
  .phone-sans { font-family: "Roboto", sans-serif; font-weight: 400; display: flex; align-items: center; justify-content: center; gap: 5px; }

  .bubble { position: absolute; border-radius: 50%; background: var(--teal); border: 4px solid rgba(255,255,255,0.55); box-shadow: 0 0 0 5px rgba(255,255,255,0.25); color: var(--white); display: flex; flex-direction: column; align-items: center; justify-content: center; font-family: "Oswald", sans-serif; font-weight: 600; text-align: center; line-height: 1; }
</style>
</head>
<body>
<main class="canvas">

  <section class="board board--kids" aria-label="Concept 1 – for kids">
    <h2 class="headline abs" style="left:22px; top:24px; color:var(--white);">
      <span class="headline__main" style="font-size:21px;">Healthy Smile</span>
      <span class="headline__sub" style="font-size:17.5px;">Is cornerstone of every age</span>
    </h2>

    <svg class="abs" style="left:0; top:0;" width="290" height="409" aria-hidden="true">
      <g stroke="var(--teal)" stroke-width="0.7" fill="none">
        <line x1="0" y1="124" x2="82" y2="146"/>
        <line x1="82" y1="146" x2="52" y2="223"/>
        <line x1="52" y1="223" x2="119" y2="287"/>
        <line x1="119" y1="287" x2="216" y2="259"/>
        <line x1="216" y1="259" x2="290" y2="280"/>
      </g>
    </svg>

    <div class="abs" role="img" aria-label="Area for a friendly cartoon tooth illustration for children" style="left:128px; top:78px; width:118px; height:180px; background:radial-gradient(ellipse at center, rgba(255,255,255,0.55) 0%, rgba(255,255,255,0.15) 60%, rgba(255,255,255,0) 100%);"></div>

    <div class="bubble" style="left:53px; top:117px; width:58px; height:58px;">
      <span style="font-size:11px;">Open</span>
      <span style="font-size:20px;">7</span>
      <span style="font-size:10px;">Days</span>
    </div>
    <div class="bubble" style="left:31px; top:202px; width:42px; height:42px;"></div>
    <div class="bubble" style="left:98px; top:266px; width:42px; height:42px;">
      <svg width="20" height="20" viewBox="0 0 20 20" aria-hidden="true"><path d="M4 10 l4 4 l8 -8" stroke="var(--white)" stroke-width="2.5" fill="none" stroke-linecap="round"/></svg>
    </div>
    <div class="bubble" style="left:187px; top:230px; width:58px; height:58px; font-size:12px;">
      <span>We</span><span>Direct</span><span>Bill</span>
    </div>

    <div class="brand abs" style="left:26px; top:327px;"><span class="brand__dot"></span>Brenvax Dental</div>

    <div class="were-in abs" style="left:197px; top:302px; background:#b7e3e2; color:var(--teal-dark); font-size:15px; padding:1px 4px;">We’re in</div>
    <div class="welcome-serif abs" style="right:32px; top:322px; color:var(--red); font-size:16px; text-align:right;">New patients<br>Welcome!</div>

    <div class="abs" style="left:31px; top:362px; width:227px; height:1px; background:var(--teal);"></div>
    <div class="phone-serif abs" style="left:0; width:290px; top:374px; justify-content:center; color:var(--teal); font-size:17px;">
      <svg width="12" height="12" viewBox="0 0 24 24" aria-hidden="true"><circle cx="12" cy="12" r="10.5" fill="none" stroke="currentColor" stroke-width="2"/><path d="M8 6.5 l2 0 l1 3 l-1.5 1 a7 7 0 0 0 4 4 l1 -1.5 l3 1 l0 2 a2 2 0 0 1 -2 1.5 a10 10 0 0 1 -9 -9 a2 2 0 0 1 1.5 -2z" fill="currentColor"/></svg>
      555 014 2270
    </div>
  </section>

  <section class="board board--teens" aria-label="Concept 2 – for teens">
    <div class="abs" style="left:0; top:0; width:287px; height:147px; background:linear-gradient(160deg, #ffffff 0%, #eef4f6 60%, #dde8ee 100%);"></div>
    <h2 class="headline abs" style="left:22px; top:20px; color:var(--teal);">
      <span class="headline__main" style="font-size:18px;">Healthy Smile</span>
      <span class="headline__sub" style="font-size:15px; color:var(--teal-deep);">Is cornerstone of every age</span>
    </h2>
    <div class="brand brand--stacked abs" style="left:206px; top:28px;"><span class="brand__dot"></span><span>Brenvax<br>Dental</span></div>

    <div class="feature abs" style="left:22px; top:73px;">
      <svg width="17" height="19" viewBox="0 0 17 19" aria-hidden="true"><rect x="1" y="3" width="15" height="15" rx="2" fill="none" stroke="var(--teal)" stroke-width="2"/><rect x="1" y="3" width="15" height="4" fill="var(--teal)"/><rect x="4" y="0" width="2" height="5" fill="var(--teal)"/><rect x="11" y="0" width="2" height="5" fill="var(--teal)"/><text x="8.5" y="16" font-size="7" text-anchor="middle" fill="var(--teal)" font-family="Oswald, sans-serif">7</text></svg>
      <span>Opening<br>7 days</span>
    </div>
    <div class="feature abs" style="left:22px; top:103px;">
      <svg width="14" height="19" viewBox="0 0 14 19" aria-hidden="true"><rect x="0" y="0" width="14" height="19" rx="1.5" fill="var(--teal)"/><g stroke="var(--white)" stroke-width="1"><line x1="3" y1="8" x2="11" y2="8"/><line x1="3" y1="11" x2="11" y2="11"/><line x1="3" y1="14" x2="11" y2="14"/></g></svg>
      <span>We direct<br>bill</span>
    </div>
    <div class="abs" role="img" aria-label="Area for a glossy tooth illustration" style="left:205px; top:66px; width:72px; height:76px; background:radial-gradient(ellipse at center, #d6e3ea 0%, rgba(221,232,238,0) 75%);"></div>

    <svg class="abs" style="left:96px; top:130px;" width="94" height="18" aria-hidden="true"><polygon points="10,0 84,0 94,18 0,18" fill="var(--grey)"/></svg>
    <div class="were-in abs" style="left:96px; width:94px; top:132px; text-align:center; color:var(--white); font-size:14px;">We’re in</div>
    <div class="welcome-sans abs" style="left:0; width:287px; top:151px; text-align:center; color:var(--white); font-size:10.5px;">New patients Welcome!</div>

    <svg class="abs" style="left:0; top:168px;" width="287" height="219" aria-hidden="true">
      <path d="M0 60 Q143 -30 287 60" fill="none" stroke="var(--white)" stroke-width="1.2"/>
    </svg>
    <div class="abs" role="img" aria-label="Photo of two smiling teenagers" style="left:0; top:177px; width:287px; height:210px; border-radius:50% 50% 0 0 / 38% 38% 0 0; background:linear-gradient(180deg, #f4f4f2 0%, #e3e1dc 55%, #c9c8c4 100%);"></div>

    <div class="phone-sans abs" style="left:0; width:287px; top:392px; color:var(--white); font-size:10px;">
      <svg width="10" height="10" viewBox="0 0 24 24" aria-hidden="true"><circle cx="12" cy="12" r="10.5" fill="none" stroke="currentColor" stroke-width="2"/><path d="M8 6.5 l2 0 l1 3 l-1.5 1 a7 7 0 0 0 4 4 l1 -1.5 l3 1 l0 2 a2 2 0 0 1 -2 1.5 a10 10 0 0 1 -9 -9 a2 2 0 0 1 1.5 -2z" fill="currentColor"/></svg>
      555 014 2270
    </div>
  </section>

  <section class="board board--seniors" aria-label="Concept 3 – for seniors">
    <div class="abs" role="img" aria-label="Photo of a smiling senior patient in a dental chair giving a thumbs up" style="left:0; top:0; width:288px; height:195px; clip-path:path('M0 0 H288 V60 Q270 170 0 190 Z'); background:linear-gradient(160deg, #eef2f3 0%, #d9e3e6 50%, #c6d6d6 100%);"></div>
    <svg class="abs" style="left:0; top:0;" width="288" height="200" aria-hidden="true">
      <path d="M288 60 Q270 170 0 190 L0 196 Q285 185 288 110 Z" fill="var(--teal)"/>
    </svg>

    <div class="feature abs" style="left:19px; top:197px;">
      <svg width="17" height="19" viewBox="0 0 17 19" aria-hidden="true"><rect x="1" y="3" width="15" height="15" rx="2" fill="none" stroke="var(--teal)" stroke-width="2"/><rect x="1" y="3" width="15" height="4" fill="var(--teal)"/><rect x="4" y="0" width="2" height="5" fill="var(--teal)"/><rect x="11" y="0" width="2" height="5" fill="var(--teal)"/><text x="8.5" y="16" font-size="7" text-anchor="middle" fill="var(--teal)" font-family="Oswald, sans-serif">7</text></svg>
      <span>Opening<br>7 days</span>
    </div>
    <div class="feature abs" style="left:98px; top:197px;">
      <svg width="14" height="19" viewBox="0 0 14 19" aria-hidden="true"><rect x="0" y="0" width="14" height="19" rx="1.5" fill="var(--teal)"/><g stroke="var(--white)" stroke-width="1"><line x1="3" y1="8" x2="11" y2="8"/><line x1="3" y1="11" x2="11" y2="11"/><line x1="3" y1="14" x2="11" y2="14"/></g></svg>
      <span>We direct<br>bill</span>
    </div>
    <div class="brand abs" style="left:188px; top:200px; font-size:14px;"><span class="brand__dot"></span>Brenvax Dental</div>

    <div class="abs" style="left:0; top:222px; width:288px; height:187px; background:radial-gradient(circle at 60% 55%, var(--aqua) 0%, var(--teal) 65%, var(--teal-deep) 100%);"></div>
    <h2 class="headline abs" style="right:18px; top:236px; color:var(--white); text-align:right;">
      <span class="headline__main" style="font-size:20px;">Healthy Smile</span>
      <span class="headline__sub" style="font-size:17px;">Is cornerstone of every age</span>
    </h2>
    <div class="abs" role="img" aria-label="Area for an illustration of a dental chair surrounded by dental tools" style="left:6px; top:266px; width:100px; height:100px; background:radial-gradient(circle, #28c0bd 0%, #1d9d9d 55%, rgba(26,154,154,0) 72%);"></div>

    <div class="were-in abs" style="right:20px; top:334px; background:var(--white); color:var(--red); font-size:13.5px; padding:1px 4px;">We’re in</div>
    <div class="welcome-serif abs" style="right:19px; top:354px; color:var(--white); font-size:15px; text-align:right;">New patients<br>Welcome!</div>
    <div class="phone-serif abs" style="left:20px; top:374px; color:var(--white); font-size:16px;">
      <svg width="11" height="11" viewBox="0 0 24 24" aria-hidden="true"><circle cx="12" cy="12" r="10.5" fill="none" stroke="currentColor" stroke-width="2"/><path d="M8 6.5 l2 0 l1 3 l-1.5 1 a7 7 0 0 0 4 4 l1 -1.5 l3 1 l0 2 a2 2 0 0 1 -2 1.5 a10 10 0 0 1 -9 -9 a2 2 0 0 1 1.5 -2z" fill="currentColor"/></svg>
      555 014 2270
    </div>
  </section>

  <section class="board board--general" aria-label="Concept 4 – for the general public">
    <div class="abs" role="img" aria-label="Photo of a smiling adult with long brown hair and crossed arms" style="left:40px; top:62px; width:249px; height:347px; border-radius:45% 45% 0 0 / 30% 30% 0 0; background:linear-gradient(180deg, #6b4433 0%, #c9a08a 35%, #d8b7a2 60%, #b8b1aa 100%);"></div>

    <h2 class="headline abs" style="left:22px; top:20px; color:var(--teal);">
      <span class="headline__main" style="font-size:18px;">Healthy Smile</span>
      <span class="headline__sub" style="font-size:15px; color:var(--teal-deep);">Is cornerstone of every age</span>
    </h2>
    <div class="brand brand--stacked abs" style="left:208px; top:28px;"><span class="brand__dot"></span><span>Brenvax<br>Dental</span></div>

    <div class="feature abs" style="left:22px; top:114px; font-size:12px;">
      <svg width="18" height="24" viewBox="0 0 14 19" aria-hidden="true"><rect x="0" y="0" width="14" height="19" rx="1.5" fill="var(--teal)"/><g stroke="var(--white)" stroke-width="1"><line x1="3" y1="8" x2="11" y2="8"/><line x1="3" y1="11" x2="11" y2="11"/><line x1="3" y1="14" x2="11" y2="14"/></g></svg>
      <span>We direct<br>bill</span>
    </div>
    <div class="feature abs" style="left:22px; top:149px; font-size:12px;">
      <svg width="22" height="25" viewBox="0 0 17 19" aria-hidden="true"><rect x="1" y="3" width="15" height="15" rx="2" fill="none" stroke="var(--teal)" stroke-width="2"/><rect x="1" y="3" width="15" height="4" fill="var(--teal)"/><rect x="4" y="0" width="2" height="5" fill="var(--teal)"/><rect x="11" y="0" width="2" height="5" fill="var(--teal)"/><text x="8.5" y="16" font-size="7" text-anchor="middle" fill="var(--teal)" font-family="Oswald, sans-serif">7</text></svg>
      <span>Opening<br>7 days</span>
    </div>

    <svg class="abs" style="left:104px; top:343px;" width="86" height="17" aria-hidden="true"><polygon points="8,0 78,0 86,17 0,17" fill="var(--white)"/></svg>
    <div class="were-in abs" style="left:104px; width:86px; top:345px; text-align:center; color:var(--red); font-size:14px;">We’re in</div>
    <div class="welcome-sans abs" style="left:0; top:360px; width:289px; height:20px; background:var(--teal); color:var(--white); font-size:13px; text-align:center; line-height:20px;">New patients Welcome!</div>
    <div class="phone-sans abs" style="left:0; width:289px; top:384px; color:var(--white); font-size:13px;">
      <svg width="12" height="12" viewBox="0 0 24 24" aria-hidden="true"><circle cx="12" cy="12" r="10.5" fill="none" stroke="currentColor" stroke-width="2"/><path d="M8 6.5 l2 0 l1 3 l-1.5 1 a7 7 0 0 0 4 4 l1 -1.5 l3 1 l0 2 a2 2 0 0 1 -2 1.5 a10 10 0 0 1 -9 -9 a2 2 0 0 1 1.5 -2z" fill="currentColor"/></svg>
      555 014 2270
    </div>
  </section>

</main>
</body>
</html>
```